I would like a flyer for the ultimate masquarade ball. This will be a PARTY! We need a flyer that will jump out and catch the attention of anyone who sees it. We would like plenty of purple and gold to be used in the flyer. The final design should communicate the ultmate, upscale, classy, exciting masquarade ball ever!

This flyer must be designed for high resolution for printing on 4" x 6" flyers.

Requirements
Must have
• Zeta Kappa Chapter Presents
Lantern Velvet & Ember MasQUErade Ball
1 March 2014
8pm - 1am
3-Course Plated Dinner
Cash Bar
RSVP By: 28 Feb 2014
Halvorsen Gaming & Downs, North Banquet Hall
DJ Tavrik
Details & Tickets: http://lanternvelvetemberball.ticketnook.example
More Info? 555-318-7726
Dress Code: Black Tie & Traditional Dress, Costumes & Masks Preferred

```html
<!DOCTYPE html>
<html lang="en">
<head>
<meta charset="utf-8">
<title>Lantern Velvet &amp; Ember Masquerade Ball</title>
<link rel="stylesheet" href="https://fonts.googleapis.com/css2?family=Cinzel:wght@400;600;700&family=Parisienne&display=swap">
<style>
  :root {
    --page: #ffffff;
    --night: #000000;
    --cream: #f1d9b4;
    --champagne: #e6c7a2;
    --cocoa: #4a2c19;
    --copper: #b5632a;
    --ember: #7a3a16;
    --smoke: #c9a88c;
    --band-top: #6e6a7c;
    --band-bottom: #1c1a2c;
    --band-edge: #2b2266;
  }
  * { margin: 0; padding: 0; box-sizing: border-box; }
  html, body {
    width: 1200px; height: 1006px; overflow: hidden;
    background: var(--page);
  }
  .flyer {
    position: absolute; left: 146px; top: 201px;
    width: 907px; height: 614px;
    background: var(--night);
    font-family: "Cinzel", serif;
    color: var(--cream);
    overflow: hidden;
  }
  .stage-backdrop {
    position: absolute; left: 0; top: 0; width: 907px; height: 390px;
    background:
      radial-gradient(circle at 75% 8%, rgba(255,240,210,.9) 0 3%, transparent 9%),
      radial-gradient(circle at 8% 3%, rgba(255,160,60,.9) 0 2.5%, transparent 6%),
      radial-gradient(circle at 35% 2%, rgba(255,170,80,.8) 0 2.5%, transparent 6%),
      radial-gradient(ellipse at 70% 40%, rgba(240,215,190,.85), transparent 45%),
      linear-gradient(90deg, var(--ember) 0%, var(--copper) 20%, #6a3216 38%, #a06844 55%, #d9c1aa 72%, #4a3a30 86%, #c99a78 100%);
  }
  .stage-backdrop::after {
    content: ""; position: absolute; left: 0; right: 0; bottom: 0; height: 70px;
    background: linear-gradient(180deg, transparent, var(--night));
  }
  .mask-art {
    position: absolute; left: 82px; top: 190px; width: 348px; height: 325px;
    border-radius: 48% 48% 40% 40% / 30% 30% 30% 30%;
    background:
      linear-gradient(180deg, #3a2418 0%, #5a3a26 40%, #2a1a12 60%, rgba(60,45,35,.55) 75%, rgba(0,0,0,0) 100%);
    box-shadow: inset 0 0 0 3px rgba(214,184,130,.35);
  }
  .centered { position: absolute; text-align: center; white-space: nowrap; }
  .presenter { left: 470px; width: 400px; top: 88px; font-size: 26px; font-weight: 700; color: var(--cocoa); }
  .presents { left: 470px; width: 400px; top: 125px; font-size: 20px; color: var(--cocoa); }
  .title-caps {
    left: 440px; width: 460px; top: 208px; height: 44px;
    font-size: 30px; font-weight: 400; line-height: 44px;
    color: var(--champagne); letter-spacing: 1px;
  }
  .title-caps .amp { font-size: 50px; line-height: 0; vertical-align: -4px; }
  .title-script {
    left: 430px; width: 460px; top: 254px; height: 46px;
    font-family: "Parisienne", cursive; font-size: 38px; line-height: 46px;
    color: var(--champagne);
  }
  .date { left: 440px; width: 460px; top: 312px; font-size: 18px; color: var(--champagne); word-spacing: 3px; }
  .dj { left: 440px; width: 460px; top: 396px; font-size: 18px; font-weight: 700; }
  .venue { left: 440px; width: 460px; top: 425px; font-size: 15px; font-weight: 600; }
  .tickets-label { left: 440px; width: 460px; top: 483px; font-size: 16px; font-weight: 600; }
  .ticket-link {
    position: absolute; left: 459px; top: 506px; width: 416px; height: 28px;
    border: 1.5px solid var(--smoke);
    font-size: 12.5px; font-weight: 600; text-align: center; line-height: 25px;
    white-space: nowrap;
  }
  .more-info { left: 440px; width: 460px; top: 544px; font-size: 16px; font-weight: 600; }
  .dinner { left: 60px; width: 380px; top: 509px; font-size: 16px; font-weight: 600; }
  .rsvp { left: 60px; width: 380px; top: 534px; font-size: 16px; font-weight: 600; }
  .dress-band {
    position: absolute; left: 0; top: 583px; width: 907px; height: 31px;
    background: linear-gradient(180deg, var(--band-top), var(--band-bottom) 55%);
    border: 1px solid var(--band-edge);
    text-align: center; font-size: 15px; font-weight: 600; line-height: 29px;
    color: var(--cream); letter-spacing: .5px;
  }
</style>
</head>
<body>
  <main class="flyer">
    <div class="stage-backdrop" role="img" aria-label="Warm curtain backdrop with glowing bokeh lights"></div>
    <div class="mask-art" role="img" aria-label="Ornate black and gold masquerade mask with its reflection"></div>

    <p class="centered presenter">Zeta Kappa Chapter</p>
    <p class="centered presents">Presents</p>
    <h1 class="centered title-caps">Lantern Velvet <span class="amp">&amp;</span></h1>
    <p class="centered title-script">Ember Masquerade Ball</p>
    <p class="centered date">1 March 2014 &nbsp;I&nbsp; 8pm - 1am</p>

    <p class="centered dj">- DJ Tavrik -</p>
    <p class="centered venue">Halvorsen Gaming &amp; Downs North Banquet Hall</p>
    <p class="centered tickets-label">Details &amp; Tickets:</p>
    <p class="ticket-link">http://lanternvelvetemberball.ticketnook.example</p>
    <p class="centered more-info">More Info : 555-318-7726</p>

    <p class="centered dinner">3-Course Plated Dinner - Cash Bar</p>
    <p class="centered rsvp">RSVP By: 28 Feb 2014</p>

    <p class="dress-band">Dress Code: Black Tie &amp; Traditional Dress, Costumes &amp; Masks Preferred</p>
  </main>
</body>
</html>
```